We need a logo for our business which is a dental clinic (i.e. dentistry).
We would lilke designs using the colour blue, green and black incorporating the words Corvasta Dental, possibly a smile or a tooth image can be considered for incorporation in the logo.

Industry/Entity Type

Dental

```html
<!DOCTYPE html>
<html lang="en">
<head>
<meta charset="utf-8">
<title>Corvasta Dental – Identity Options</title>
<link href="https://fonts.googleapis.com/css2?family=Oswald:wght@300;400&display=swap" rel="stylesheet">
<style>
  :root {
    --board: #ececec;
    --blue: #00aeef;
    --blue-deep: #1e9ad6;
    --green: #8cc63f;
    --green-soft: #a9d46f;
    --ink: #111111;
    --white: #ffffff;
    --label: #8a8a8a;
  }
  * { margin: 0; padding: 0; box-sizing: border-box; }
  html, body { width: 1047px; height: 1200px; overflow: hidden; }
  body {
    background: var(--board);
    font-family: "Oswald", "Arial Narrow", sans-serif;
    position: relative;
  }
  .card {
    position: absolute;
    top: 87px;
    width: 318px;
    height: 543px;
    background: var(--white);
    box-shadow: 3px 4px 7px rgba(0,0,0,0.35);
    overflow: hidden;
  }
  .card--one { left: 122px; }
  .card--two { left: 593px; }
  .card__wave { position: absolute; left: 0; top: 0; }
  .card__mark {
    position: absolute; left: 107px; top: 36px;
    width: 104px; height: 104px; border-radius: 50%;
    background: var(--blue);
  }
  .card__brand {
    position: absolute; left: 0; width: 100%; top: 160px;
    text-align: center; font-size: 36px; font-weight: 400; color: var(--ink);
    letter-spacing: 0.5px; line-height: 50px; white-space: nowrap;
  }
  .card__brand--caps { font-size: 31px; letter-spacing: 0.3px; }
  .card__person {
    position: absolute; left: 0; width: 100%; top: 294px;
    text-align: center; font-size: 27px; font-weight: 300; color: var(--white);
  }
  .card__rule {
    position: absolute; left: 22px; width: 278px;
    border-top: 1px dashed var(--green-soft);
  }
  .card__rule--top { top: 345px; }
  .card__rule--bottom { top: 441px; }
  .contact {
    position: absolute; left: 64px; top: 355px; list-style: none;
    color: var(--white); font-size: 16px; font-weight: 300;
  }
  .contact li { height: 24.5px; display: flex; align-items: center; }
  .contact svg { width: 14px; height: 14px; margin-right: 8px; flex: none; }
  .contact .phone-number { letter-spacing: 2.5px; }
  .address {
    position: absolute; left: 0; width: 100%; top: 455px;
    text-align: center; color: var(--white); font-size: 16px; font-weight: 300; line-height: 20px;
  }
  .address svg { display: block; margin: 0 auto 2px; width: 12px; height: 14px; }
  .logo {
    position: absolute; top: 759px; width: 450px; text-align: center;
  }
  .logo--one { left: 40px; }
  .logo--two { left: 556px; }
  .logo__mark {
    width: 206px; height: 206px; border-radius: 50%;
    background: var(--blue); margin: 0 auto;
  }
  .logo__name {
    height: 110px; margin-top: 20px;
    display: flex; align-items: flex-end; justify-content: center;
    font-weight: 400; color: var(--ink); line-height: 1; white-space: nowrap;
  }
  .logo__name--mixed { font-size: 72px; letter-spacing: 0.5px; }
  .logo__name--caps { font-size: 61px; letter-spacing: 0.3px; padding-bottom: 6px; }
  .option-number {
    position: absolute; top: 1135px; width: 60px; text-align: center;
    font-size: 42px; font-weight: 300; color: var(--label);
  }
  .option-number--one { left: 245px; }
  .option-number--two { left: 753px; }
</style>
</head>
<body>

<svg width="0" height="0" style="position:absolute">
  <defs>
    <symbol id="icon-phone" viewBox="0 0 14 14"><path d="M3 1 L5 4 L4 5.5 C5 7.5 6.5 9 8.5 10 L10 9 L13 11 L11.5 13 C6 12.5 1.5 8 1 2.5 Z" fill="var(--green)"/></symbol>
    <symbol id="icon-mail" viewBox="0 0 14 14"><rect x="1" y="3" width="12" height="8" fill="none" stroke="var(--green)" stroke-width="1.3"/><path d="M1 3 L7 8 L13 3" fill="none" stroke="var(--green)" stroke-width="1.3"/></symbol>
    <symbol id="icon-search" viewBox="0 0 14 14"><circle cx="6" cy="6" r="4" fill="none" stroke="var(--green)" stroke-width="1.5"/><path d="M9 9 L13 13" stroke="var(--green)" stroke-width="1.8"/></symbol>
    <symbol id="icon-pin" viewBox="0 0 12 14"><path d="M6 1 C3 1 1.5 3 1.5 5 C1.5 8 6 13 6 13 C6 13 10.5 8 10.5 5 C10.5 3 9 1 6 1 Z" fill="var(--green)"/><circle cx="6" cy="5" r="1.6" fill="var(--blue)"/></symbol>
  </defs>
</svg>

<div class="card card--one">
  <svg class="card__wave" width="318" height="543" viewBox="0 0 318 543">
    <path d="M0 264 C110 238 200 195 318 216 L318 543 L0 543 Z" fill="var(--green-soft)"/>
    <path d="M0 283 C110 252 205 200 318 221 L318 543 L0 543 Z" fill="var(--blue)"/>
  </svg>
  <div class="card__mark"></div>
  <div class="card__brand">Corvasta Dental</div>
  <div class="card__person">Dr. Name Lastname</div>
  <div class="card__rule card__rule--top"></div>
  <ul class="contact">
    <li><svg><use href="#icon-phone"/></svg><span class="phone-number">(08) 7140 2286</span></li>
    <li><svg><use href="#icon-mail"/></svg>name@corvastadental.com</li>
    <li><svg><use href="#icon-search"/></svg>corvastadental.com</li>
  </ul>
  <div class="card__rule card__rule--bottom"></div>
  <div class="address"><svg><use href="#icon-pin"/></svg>18 Harbour View Rd<br>Corvasta, SA, 5170</div>
</div>

<div class="card card--two">
  <svg class="card__wave" width="318" height="543" viewBox="0 0 318 543">
    <path d="M0 264 C110 238 200 195 318 216 L318 543 L0 543 Z" fill="var(--green-soft)"/>
    <path d="M0 283 C110 252 205 200 318 221 L318 543 L0 543 Z" fill="var(--blue)"/>
  </svg>
  <div class="card__mark"></div>
  <div class="card__brand card__brand--caps">CORVASTA DENTAL</div>
  <div class="card__person">Dr. Name Lastname</div>
  <div class="card__rule card__rule--top"></div>
  <ul class="contact">
    <li><svg><use href="#icon-phone"/></svg><span class="phone-number">(08) 7140 2286</span></li>
    <li><svg><use href="#icon-mail"/></svg>name@corvastadental.com</li>
    <li><svg><use href="#icon-search"/></svg>corvastadental.com</li>
  </ul>
  <div class="card__rule card__rule--bottom"></div>
  <div class="address"><svg><use href="#icon-pin"/></svg>18 Harbour View Rd<br>Corvasta, SA, 5170</div>
</div>

<div class="logo logo--one">
  <div class="logo__mark"></div>
  <div class="logo__name logo__name--mixed">Corvasta Dental</div>
</div>

<div class="logo logo--two">
  <div class="logo__mark"></div>
  <div class="logo__name logo__name--caps">CORVASTA DENTAL</div>
</div>

<div class="option-number option-number--one">1</div>
<div class="option-number option-number--two">2</div>

</body>
</html>
```